Jolie Plume Gourmet Brie Packaging

I developed and market a 10oz wheel (7inch dia) and a 6 oz wheel (5 inch dia) Gourmet Brie Cheese Line. They are all double cream bries, topped with decadent concoctions and wrapped with buttery puff pastry. They are frozen and vacuum sealed. They are sold in markets as a frozen item. I am looking for a paper "slip"/ wrap to house the brie that would have my logo, nutritional info, and cooking instructions in a mod fresh background. The company Name is Jolie Plume (bright spoon). and the Product if Gourmet Brie. I would like to wrapper to be able to house both sizes so I dont double my costs. My Logo for Jolie Plume is a Red sketched chicken in the middle of the name. The writing is in Black (le Carte pen is the font I used)
My website is brightspoon-events.example.
Updates

I have added a logo file for the packaging.  The logo should be the jolie plume chicken and not bright spoon events.  Also, I would like the style and colors to match with this  - THANKS!

I have updated to Jolie Plume Logo - Please make the change to your designs.  I will be selecting design a week from today.  The choosen design may require a few edits, but minimal. Thanks!

Reason: I will be choosing Design April 2. Please have any changes, designs and or ideas to Jolie Plume by then. Thanks you all so much for what you submitted....I like them all!!!!

Target Market(s)

Gourmet Food/Wine Shops /upscale grocery.

Industry/Entity Type

Cooking

Requirements
Must have
• Ingredients, Nutritional info, directions.
Logo and name.

```html
<!DOCTYPE html>
<html lang="en">
<head>
<meta charset="utf-8">
<title>Jolie Plume Gourmet Brie Wrapper</title>
<link rel="stylesheet" href="https://fonts.googleapis.com/css2?family=Federant&family=Gilda+Display&display=swap">
<style>
  :root {
    --maroon: #5c2329;
    --maroon-dark: #2e1a1c;
    --cream: #fffcb0;
    --butter: #ffe98c;
    --gold: #fff08f;
    --board: #f4e6a0;
    --ink: #1a1a1a;
    --page: #ffffff;
  }
  * { margin: 0; padding: 0; box-sizing: border-box; }
  html, body { width: 1200px; height: 900px; overflow: hidden; background: var(--page); }
  .canvas { position: relative; width: 1200px; height: 900px; }
  .side-label {
    position: absolute; top: 42px; width: 200px; text-align: center;
    font-family: "Gilda Display", serif; font-size: 24px; color: var(--ink);
  }
  .side-label.back { left: 170px; }
  .side-label.front { left: 836px; }
  .panel { position: absolute; top: 70px; width: 490px; height: 612px; }
  .panel.back { left: 58px; }
  .panel.front { left: 666px; }
  .panel svg { display: block; width: 100%; height: 100%; }
  .title { font-family: "Federant", serif; fill: var(--gold); stroke: var(--maroon); stroke-width: 1.2px; paint-order: stroke; }
  .flavour { font-family: "Federant", serif; fill: var(--maroon-dark); font-weight: 700; }
  .body-text { font-family: "Gilda Display", serif; fill: var(--maroon); }
  .brand-name { font-family: "Gilda Display", serif; }
</style>
</head>
<body>
<main class="canvas">
  <div class="side-label back">Back</div>
  <div class="side-label front">Front</div>

  <section class="panel back">
    <svg viewBox="0 0 490 612" aria-label="Back of wrapper">
      <defs>
        <radialGradient id="seal-soft" cx="0.5" cy="0.4" r="0.6">
          <stop offset="0" stop-color="#4a2025"/>
          <stop offset="1" stop-color="#2e1a1c"/>
        </radialGradient>
      </defs>
      <rect class="wrapper-ground" width="490" height="612" fill="var(--cream)"/>
      <rect class="edge-stripe" x="19" y="0" width="8" height="612" fill="var(--maroon)"/>
      <rect class="edge-stripe" x="463" y="0" width="8" height="612" fill="var(--maroon)"/>

      <circle class="seal-ring" cx="244" cy="146" r="96" fill="var(--gold)" stroke="var(--maroon)" stroke-width="2"/>
      <circle class="seal" cx="244" cy="146" r="86" fill="url(#seal-soft)" role="img" aria-label="Maroon and dark argyle diamond pattern"/>
      <ellipse class="dish-frame" cx="242" cy="212" rx="56" ry="38" fill="var(--gold)" stroke="var(--maroon)" stroke-width="3"/>
      <ellipse class="dish-art" cx="242" cy="212" rx="44" ry="28" fill="var(--board)" role="img" aria-label="Sketch of baked brie in pastry on a board"/>

      <rect class="flavour-tag" x="176" y="47" width="138" height="43" rx="4" fill="var(--cream)" stroke="var(--maroon)" stroke-width="4"/>
      <text class="flavour" x="245" y="76" text-anchor="middle" font-size="19">Mushroom</text>
      <text class="title" x="242" y="120" text-anchor="middle" font-size="26" textLength="112" lengthAdjust="spacingAndGlyphs">Gourmet</text>
      <text class="title" x="242" y="142" text-anchor="middle" font-size="26" textLength="168" lengthAdjust="spacingAndGlyphs">Brie Cheese</text>

      <text class="body-text" x="242" y="266" text-anchor="middle" font-size="7.5">Ingredients: Button and Baby Bellas, Shallots, Sherry</text>
      <text class="body-text" x="240" y="295" text-anchor="middle" font-size="15" font-weight="700" text-decoration="underline">To Serve:</text>

      <g class="serve-steps body-text" font-size="11">
        <text x="98" y="318" font-size="18">1.</text>
        <text x="121" y="316">Remove from Packaging and thaw in refrigerator</text>
        <text x="121" y="330">overnight or on counter for 2 hours before baking.</text>
        <text x="98" y="357" font-size="18">2.</text>
        <text x="121" y="356">Place on Baking Pan and brush with a beaten egg</text>
        <text x="98" y="389" font-size="18">3.</text>
        <text x="121" y="383">Bake at 400 degrees for 25-30 minutes until</text>
        <text x="121" y="397">pastry is puffed and golden.</text>
        <text x="98" y="425" font-size="18">4.</text>
        <text x="121" y="423">Let stand for 15 minutes before serving.</text>
      </g>

      <text class="body-text" x="242" y="457" text-anchor="middle" font-size="11">Keep Frozen</text>
      <rect class="nutrition-box" x="118" y="461" width="254" height="100" fill="none" stroke="var(--maroon)" stroke-width="1.5"/>
      <text class="body-text" x="245" y="518" text-anchor="middle" font-size="19">(NUTRITIONAL INFO)</text>

      <text class="brand-name" x="242" y="596" text-anchor="middle" font-size="24" fill="var(--ink)">Jolie Plume</text>
    </svg>
  </section>

  <section class="panel front">
    <svg viewBox="0 0 490 612" aria-label="Front of wrapper">
      <defs>
        <linearGradient id="bg-soft-front" x1="0" y1="0" x2="1" y2="0">
          <stop offset="0" stop-color="#fffbb0"/>
          <stop offset="0.25" stop-color="#ffea8e"/>
          <stop offset="0.5" stop-color="#fffbb0"/>
          <stop offset="0.75" stop-color="#ffea8e"/>
          <stop offset="1" stop-color="#fffbb0"/>
        </linearGradient>
        <radialGradient id="seal-soft-front" cx="0.5" cy="0.45" r="0.6">
          <stop offset="0" stop-color="#52222a"/>
          <stop offset="1" stop-color="#2e1a1c"/>
        </radialGradient>
      </defs>
      <rect class="wrapper-ground" width="490" height="612" fill="url(#bg-soft-front)" role="img" aria-label="Soft diamond argyle pattern in butter and pale yellow"/>
      <rect class="edge-stripe" x="17" y="0" width="9" height="612" fill="var(--maroon)"/>
      <rect class="edge-stripe" x="465" y="0" width="9" height="612" fill="var(--maroon)"/>

      <circle class="seal-outline" cx="246" cy="290" r="224" fill="none" stroke="var(--maroon)" stroke-width="3"/>
      <circle class="seal-ring" cx="246" cy="290" r="220" fill="var(--gold)"/>
      <circle class="seal" cx="246" cy="288" r="198" fill="url(#seal-soft-front)" role="img" aria-label="Maroon and dark argyle diamond pattern"/>

      <ellipse class="dish-frame" cx="244" cy="494" rx="120" ry="90" fill="var(--gold)" stroke="var(--maroon)" stroke-width="10"/>
      <ellipse class="dish-art" cx="244" cy="490" rx="94" ry="62" fill="var(--board)" role="img" aria-label="Sketch of baked brie in pastry on a board"/>

      <text class="brand-name" x="244" y="212" text-anchor="middle" font-size="26" fill="var(--cream)">Jolie Plume</text>
      <text class="title" x="244" y="288" text-anchor="middle" font-size="62" stroke-width="2" textLength="256" lengthAdjust="spacingAndGlyphs">Gourmet</text>
      <text class="title" x="244" y="332" text-anchor="middle" font-size="62" stroke-width="2" textLength="370" lengthAdjust="spacingAndGlyphs">Brie Cheese</text>

      <rect class="flavour-tag" x="182" y="536" width="129" height="50" rx="4" fill="var(--cream)" stroke="var(--maroon)" stroke-width="6"/>
      <text class="flavour" x="246" y="568" text-anchor="middle" font-size="18">Mushroom</text>
      <text class="body-text" x="240" y="604" text-anchor="middle" font-size="9">Keep Frozen</text>
    </svg>
  </section>
</main>
</body>
</html>
```